Need a Marketing System Program Overview Flyer

Our business, Builder Momentum Network, helps General Contractors and home improvement businesses to generate high quality leads, acquire new customers, and improve their overall online presence.

The system includes a...
- High Converting Website
- SEO & Online Listings Management
- Strategic PPC Advertising
- Email Marketing and Automation
- Social Media Management & Retargeting Campaigns
- Reputation Management
- Tracking and Reporting

The Brochure or flyer needs to have a very professional and high class look that wows the potential customers when overviewing the program.

It needs to give a clear explanation of the program while simultaneously having the very best design concept that pulls the reader in.

I've attached our branding guide, logos and additional information...

Our site is currently being staged at www.ridgevantix.com/BMN

```html
<!DOCTYPE html>
<html lang="en">
<head>
<meta charset="utf-8">
<title>Builder Momentum Network – Program Overview</title>
<link href="https://fonts.googleapis.com/css2?family=Bebas+Neue&family=Montserrat:wght@400;500;600;700&display=swap" rel="stylesheet">
<style>
  :root{
    --gold:#d9b44a;
    --ink:#0d0d0d;
    --paper:#ffffff;
    --stage:#eeeeee;
    --text:#1a1a1a;
    --muted:#333333;
  }
  *{margin:0;padding:0;box-sizing:border-box}
  html,body{width:800px;height:1200px;overflow:hidden;background:var(--stage)}
  body{font-family:"Montserrat",sans-serif;color:var(--text)}
  .flyer{position:absolute;left:20px;top:62px;width:760px;height:1075px;background:var(--paper);overflow:hidden;box-shadow:0 6px 14px rgba(0,0,0,.18)}
  .abs{position:absolute}

  .brand{left:43px;top:50px;display:flex;align-items:center;gap:10px}
  .brand-mark{width:22px;height:22px;border-radius:50%;background:var(--ink)}
  .brand-name{font-family:"Montserrat",sans-serif;font-weight:700;font-size:21px;line-height:1.1;color:var(--ink);letter-spacing:.3px}

  .rule-top{left:0;top:176px;width:345px;height:6px;background:var(--gold)}
  .hero{left:0;top:187px;width:760px;height:334px;background:var(--ink)}
  .hero-photo{left:0;top:0;width:760px;height:521px}

  .headline{left:43px;top:234px;font-family:"Bebas Neue",sans-serif;color:var(--paper);line-height:1}
  .headline .l1{font-size:48px;letter-spacing:.5px}
  .headline .l1 span{font-family:"Montserrat",sans-serif;font-weight:400;font-size:30px}
  .headline .l2{font-size:48px;color:var(--gold);margin-top:-2px}
  .headline .l3{font-size:36px;color:var(--gold);margin-top:2px}
  .headline .l4{font-family:"Montserrat",sans-serif;font-size:29px;margin-top:2px}
  .headline-rule{left:43px;top:415px;width:85px;height:3px;background:var(--gold)}
  .tagline{left:43px;top:443px;background:var(--paper);color:var(--ink);font-weight:700;font-size:14px;padding:2px 8px}
  .tagline-sub{left:45px;top:470px;color:var(--paper);font-size:10px}

  .rule-mid{left:0;top:524px;width:760px;height:6px;background:var(--gold)}

  .section-title{font-weight:700;font-size:22px;color:var(--ink)}
  .section-title span{color:var(--gold);font-weight:500}
  .section-rule{width:38px;height:2px;background:var(--ink)}

  .about{left:43px;width:304px}
  .lead{font-size:13px;line-height:1.25}
  .lead strong{font-weight:700}
  .lead em{font-style:normal;color:var(--gold);font-weight:700}
  .body-copy{font-size:9.6px;line-height:1.3;text-align:justify;color:var(--muted)}

  .system{display:flex;align-items:flex-start;gap:8px;font-size:12.5px;line-height:1.2;font-weight:500;width:180px}
  .sys-icon{flex:none;width:27px;height:27px;border-radius:50%;border:2px solid var(--gold);display:flex;align-items:center;justify-content:center}
  .sys-icon i{width:11px;height:11px;border-radius:2px;border:1.5px solid var(--ink)}

  .wheel{left:447px;top:803px;width:216px;height:216px}

  .footer{left:0;top:1015px;width:475px;height:60px;background:var(--ink);clip-path:polygon(0 0,440px 0,100% 100%,0 100%);color:var(--paper);display:flex;align-items:center;padding-left:43px;gap:10px}
  .phone{font-size:20px;font-weight:500;display:flex;align-items:center;gap:6px}
  .divider{width:1px;height:22px;background:var(--paper)}
  .web{font-size:10px}
  .rule-bottom{left:475px;top:1055px;width:285px;height:5px;background:var(--gold)}
  .follow{left:583px;top:1032px;font-size:10px;display:flex;align-items:center;gap:7px}
  .follow i{width:16px;height:16px;background:var(--gold);display:inline-block}
</style>
</head>
<body>
<main class="flyer">

  <div class="abs brand">
    <span class="brand-mark"></span>
    <span class="brand-name">Builder Momentum<br>Network</span>
  </div>

  <div class="abs rule-top"></div>
  <div class="abs hero"></div>

  <svg class="abs hero-photo" viewBox="0 0 760 521" role="img" aria-label="Construction crew silhouetted on scaffolding assembling a house frame against a sunset sky">
    <defs>
      <linearGradient id="sky" x1="0" y1="0" x2="0" y2="1">
        <stop offset="0" stop-color="#6d7483"/>
        <stop offset=".5" stop-color="#9a8a78"/>
        <stop offset=".8" stop-color="#e0953a"/>
        <stop offset="1" stop-color="#1a120c"/>
      </linearGradient>
      <linearGradient id="fade" x1="0" y1="0" x2="1" y2="0">
        <stop offset="0" stop-color="#0d0d0d" stop-opacity="1"/>
        <stop offset=".25" stop-color="#0d0d0d" stop-opacity="0"/>
      </linearGradient>
    </defs>
    <polygon points="358,176 603,24 760,114 760,521 358,521" fill="url(#sky)"/>
    <polygon points="358,176 603,24 760,114 760,521 358,521" fill="url(#fade)"/>
    <polyline points="345,178 603,16 760,108" fill="none" stroke="#d9b44a" stroke-width="4"/>
  </svg>

  <h1 class="abs headline">
    <div class="l1">ACCELERATE <span>YOUR</span></div>
    <div class="l2">LEAD GENERATION</div>
    <div class="l3">WHILE INCREASING SALES</div>
    <div class="l4">And Reducing Costs</div>
  </h1>
  <div class="abs headline-rule"></div>
  <div class="abs tagline">Our 7-Point Builder Momentum Network</div>
  <div class="abs tagline-sub">Will Show You What Return On Investment Truly Means!</div>

  <div class="abs rule-mid"></div>

  <section class="abs about" style="top:548px">
    <h2 class="section-title">ABOUT <span>US</span></h2>
    <div class="section-rule" style="margin:9px 0 20px"></div>
    <p class="lead">Take Your Business To The Next Level<br><strong>Accelerate Your Lead Generation<br>Under One Roof - BMN</strong></p>
    <p class="body-copy" style="margin-top:12px">BMN is years of general contractors marketing experience and accumulated learning from working with local clients. This growth system is designed in such a way that all your digital marketing strategies arise from a single source – saving you time, money and frustration.</p>
    <p class="lead" style="margin-top:20px">How We Generate Our Contractor Leads<br><strong>We'll Build A <em>Custom Growth<br>System</em> That Delivers The Customers<br>You Want</strong></p>
    <div class="section-rule" style="margin:9px 0 16px"></div>
    <p class="body-copy">BMN helps General Contractor businesses of all sizes to increase their revenue by generating new customers and leads online. Through this process, we have developed a 7 POINT SYSTEM that hits all the points of the digital marketing eco-system. The Builder Momentum Network is specially designed to not only bring visitors to your website, but we have engineered a PROVEN system that turns those visitors into Leads and Customers. We're not a cookie-cutter company – and we don't offer DIY software that makes you do all the work. We create a custom digital marketing solution designed to meet your specific needs and to fit your budget.</p>
  </section>

  <section class="abs" style="left:388px;top:548px">
    <h2 class="section-title">OUR <span>SYSTEMS</span></h2>
    <div class="section-rule" style="margin-top:9px"></div>
  </section>

  <div class="abs system" style="left:388px;top:617px"><span class="sys-icon"><i></i></span>High Converting Website</div>
  <div class="abs system" style="left:388px;top:662px"><span class="sys-icon"><i></i></span>SEO &amp; Online Listings Management</div>
  <div class="abs system" style="left:388px;top:709px"><span class="sys-icon"><i></i></span>Strategic PPC Advertising</div>
  <div class="abs system" style="left:388px;top:755px"><span class="sys-icon"><i></i></span>Email Marketing and Automation</div>
  <div class="abs system" style="left:586px;top:617px;width:160px"><span class="sys-icon"><i></i></span>Social Media Management &amp; Retargeting Campaigns</div>
  <div class="abs system" style="left:586px;top:690px;width:160px"><span class="sys-icon"><i></i></span>Reputation Management</div>
  <div class="abs system" style="left:586px;top:735px;width:160px"><span class="sys-icon"><i></i></span>Tracking and Reporting</div>

  <svg class="abs wheel" viewBox="0 0 216 216" role="img" aria-label="Rocket launching through a seven-segment ring of marketing service icons">
    <defs>
      <radialGradient id="core" cx=".5" cy=".5" r=".5">
        <stop offset="0" stop-color="#f3a73a"/>
        <stop offset=".6" stop-color="#e8573a"/>
        <stop offset="1" stop-color="#ffffff"/>
      </radialGradient>
    </defs>
    <circle cx="108" cy="108" r="104" fill="#ffffff" stroke="#222" stroke-width="3"/>
    <circle cx="108" cy="108" r="64" fill="url(#core)" stroke="#222" stroke-width="2"/>
  </svg>

  <footer class="abs footer">
    <span class="phone">
      <svg width="16" height="16" viewBox="0 0 24 24" aria-hidden="true"><path d="M6.6 10.8a15 15 0 006.6 6.6l2.2-2.2a1 1 0 011-.25 11.4 11.4 0 003.6.6 1 1 0 011 1V20a1 1 0 01-1 1A17 17 0 013 4a1 1 0 011-1h3.5a1 1 0 011 1c0 1.25.2 2.45.6 3.6a1 1 0 01-.25 1z" fill="#d9b44a"/></svg>
      (555) 318-4720
    </span>
    <span class="divider"></span>
    <span class="web">www.ridgevantix.com</span>
  </footer>
  <div class="abs rule-bottom"></div>
  <div class="abs follow">Follow Us <i></i><i></i><i></i></div>

</main>
</body>
</html>
```